Adult toys brand needs a Packaging Design

- We need design for packaging for Adult Toys brand.
- Packaging is for vibrators.
- Design needs to be clean and modern, minimal
- Main color is white and purple.
- Brand name is KOVEL, logo is attached.
- Dielines are attached. The packaging consists of the box and the sleeve that goes on the box. We need design for sleeve ONLY.
Updates

Industry/Entity Type

Adult

Font styles to use
Sans Serif

Requirements
Must have
• - Logo
• - item picture (purple version)
• - web address (kovel.example or www.kovel.example)
• - main features

```html
<!DOCTYPE html>
<html lang="en">
<head>
<meta charset="utf-8">
<title>KOVEL Sleeve Packaging</title>
<link rel="stylesheet" href="https://fonts.googleapis.com/css2?family=Open+Sans:wght@400;600;700&family=Cormorant+Garamond:ital@1&family=Great+Vibes&display=swap">
<style>
  :root {
    --purple: #5b2a9e;
    --purple-light: #8f5ad0;
    --magenta: #e5188f;
    --lilac: #c57ae6;
    --lavender: #f6ecfb;
    --ink: #2b2b2b;
    --line: #8a8a8a;
    --bg: #ffffff;
  }
  * { box-sizing: border-box; margin: 0; padding: 0; }
  html, body { width: 1200px; height: 1200px; overflow: hidden; background: var(--bg); }
  .canvas { position: relative; width: 1200px; height: 1200px; }
  .sleeve {
    position: absolute; left: 17px; top: 130px; height: 940px;
    display: flex; border: 1px solid var(--line);
  }
  .panel { position: relative; height: 100%; background: #fff; border-right: 1px solid var(--line); }
  .panel:last-child { border-right: none; }
  .panel--back { width: 340px; }
  .panel--features { width: 216px; }
  .panel--front { width: 340px; }
  .panel--side { width: 270px; background: linear-gradient(180deg, #fbf5fd 0%, var(--lavender) 100%); }

  .product-visual {
    position: absolute; left: 50%; transform: translateX(-50%);
    border-radius: 50% 50% 40% 40% / 18% 18% 10% 10%;
    background: linear-gradient(180deg, var(--purple-light) 0%, var(--purple) 78%, #ffffff 80%, #f3eef7 100%);
    box-shadow: 0 0 60px 30px rgba(218, 180, 240, .45);
  }
  .panel--back .product-visual { top: 98px; width: 60px; height: 290px; }
  .panel--front .product-visual { top: 88px; width: 120px; height: 590px; }

  .brand {
    position: absolute; left: 0; right: 0; text-align: center;
    font-family: 'Open Sans', sans-serif; font-weight: 700; color: var(--ink);
    display: flex; align-items: center; justify-content: center; gap: 8px;
  }
  .brand__dot { border-radius: 50%; background: var(--magenta); }
  .panel--back .brand { top: 440px; font-size: 40px; }
  .panel--back .brand__dot { width: 12px; height: 12px; }
  .panel--front .brand { top: 760px; font-size: 64px; }
  .panel--front .brand__dot { width: 18px; height: 18px; }

  .description {
    position: absolute; left: 45px; right: 45px; top: 552px;
    font-family: 'Cormorant Garamond', serif; font-style: italic;
    font-size: 9px; line-height: 13px; color: var(--lilac); text-align: justify;
  }
  .feature-list {
    position: absolute; left: 55px; right: 30px; top: 690px;
    font-family: 'Cormorant Garamond', serif; font-style: italic;
    font-size: 9px; line-height: 13px; color: var(--lilac);
  }
  .certs { position: absolute; right: 55px; top: 852px; display: flex; gap: 8px; align-items: center; }
  .cert { width: 14px; height: 14px; border: 1.5px solid var(--ink); }
  .cert--wide { width: 30px; }
  .origin {
    position: absolute; right: 56px; top: 880px;
    font-family: 'Open Sans', sans-serif; font-size: 11px; color: var(--ink);
  }

  .feature { position: absolute; left: 0; right: 0; text-align: center; }
  .feature svg { display: block; margin: 0 auto 10px; }
  .feature__label {
    font-family: 'Open Sans', sans-serif; font-size: 12.5px; letter-spacing: .4px;
    color: var(--magenta); line-height: 14px;
  }
  .feature--ergonomic { top: 120px; }
  .feature--quiet { top: 312px; }
  .feature--waterproof { top: 505px; }
  .feature--luxurious { top: 700px; }
  .web {
    position: absolute; left: 0; right: 0; top: 885px; text-align: center;
    font-family: 'Open Sans', sans-serif; font-size: 11px; color: var(--lilac);
  }

  .tagline {
    position: absolute; left: 135px; top: 470px;
    transform: translate(-50%, -50%) rotate(-90deg);
    white-space: nowrap;
    font-family: 'Great Vibes', cursive; font-size: 62px; color: var(--lilac);
  }
</style>
</head>
<body>
<div class="canvas">
  <div class="sleeve">
    <section class="panel panel--back">
      <div class="product-visual" role="img" aria-label="Purple rabbit vibrator with soft lavender lotus flowers behind it"></div>
      <div class="brand"><span class="brand__dot"></span>KOVEL</div>
      <p class="description">This large life-like rabbit vibe is design to reach your G-spot with ease and proportion, it feels just like the real thing, two motors with 11 powerful functions and control seperately, while the realistic tip tickles that sweet spot in just the right way, enhanced by a luxurious silicone texture that mimics real skin. Take this beauty into the bath or shower with you, as it's completly waterproof and clean up in a snap with toy cleaner and a warm water rinse.</p>
      <ul class="feature-list">
        <li>Realistic rabbit vibe</li>
        <li>11 powerful functions* 2 motors</li>
        <li>Gently curved shaft for reaching G-spot</li>
        <li>Unique forked handle shape for easy grip</li>
        <li>Made with luxuriously smooth silicone</li>
        <li>191mm total length, 73 mm insertable length, 37mm width</li>
        <li>Phthalate &amp; latex free</li>
        <li>Completely waterproof &amp; submersible</li>
        <li>Fully rechargeable, USB cable included</li>
      </ul>
      <div class="certs">
        <span class="cert"></span><span class="cert cert--wide"></span><span class="cert"></span><span class="cert"></span>
      </div>
      <div class="origin">MADE IN CHINA</div>
    </section>

    <section class="panel panel--features">
      <div class="feature feature--ergonomic">
        <svg width="70" height="70" viewBox="0 0 70 70"><circle cx="35" cy="35" r="31" fill="none" stroke="var(--magenta)" stroke-width="4"/><path d="M20 42 Q30 52 44 40 L50 26" fill="none" stroke="var(--magenta)" stroke-width="5" stroke-linecap="round"/><path d="M34 36 L42 20 M28 34 L34 18" stroke="var(--magenta)" stroke-width="4" stroke-linecap="round"/></svg>
        <div class="feature__label">ERGONOMIC</div>
      </div>
      <div class="feature feature--quiet">
        <svg width="70" height="70" viewBox="0 0 70 70"><circle cx="35" cy="35" r="31" fill="none" stroke="var(--magenta)" stroke-width="4"/><path d="M22 28 H30 L42 18 V52 L30 42 H22 Z" fill="var(--magenta)"/><path d="M18 18 L52 52" stroke="#fff" stroke-width="6"/><path d="M18 18 L52 52" stroke="var(--magenta)" stroke-width="3"/></svg>
        <div class="feature__label">EXTREMELY QUIET<br>&lt;49dB</div>
      </div>
      <div class="feature feature--waterproof">
        <svg width="70" height="70" viewBox="0 0 70 70"><circle cx="35" cy="35" r="31" fill="none" stroke="var(--magenta)" stroke-width="4"/><path d="M35 18 C41 28 46 34 46 41 A11 11 0 0 1 24 41 C24 34 29 28 35 18 Z" fill="var(--magenta)"/></svg>
        <div class="feature__label">100% WATERPROOF</div>
      </div>
      <div class="feature feature--luxurious">
        <svg width="70" height="70" viewBox="0 0 70 70"><circle cx="35" cy="35" r="31" fill="none" stroke="var(--magenta)" stroke-width="4"/><path d="M22 31 L28 24 H42 L48 31 L35 48 Z M22 31 H48 M28 24 L32 31 L35 48 L38 31 L42 24" fill="none" stroke="var(--magenta)" stroke-width="2.5" stroke-linejoin="round"/></svg>
        <div class="feature__label">LUXURIOUS</div>
      </div>
      <div class="web">www.kovel.example</div>
    </section>

    <section class="panel panel--front">
      <div class="product-visual" role="img" aria-label="Large purple rabbit vibrator with soft lavender lotus flowers behind it"></div>
      <div class="brand"><span class="brand__dot"></span>KOVEL</div>
    </section>

    <section class="panel panel--side">
      <div class="tagline">Enjoy Your Passionate Life</div>
    </section>
  </div>
</div>
</body>
</html>
```